Corporate Business Card Design Project

..Hi designers!
I have established a consultancy within strategic communnications, for which I need a business card design - I've seen some of the things you do in here, and they're great! I'll provide some information in the following:
Name: BrookLedger
Tagline: Guiding Dialogue
Service: Strategic communications consulting (primariy internal communication and optimizing): various organisations - e.g. SMEs, NGOs and NPOs - are offered an analysis of their current efforts and, on the basis of that, management consulting tailored their unique challenges and needs.
It's a sole proprietorship - for now! - but it's my plan to employ 5-20 persons over the years. Therefore the card should NOT symbolize a start-up, but communicate a well-established, serious consultancy. Hence, it should also apply to serious companies and organizations - think Tolvik or Hadley Prewitt Group (both as sender and receiver) ;)
The design should accordingly have a formal, conservative, stylish, corporate, clean look! and ditto colors, eg. black, grey, white etc - corresponding to the logo. The only colour that can appear is the same orange contrast as in my logo (see attachement). Not too bold or dramatic fonds or letters.
I choose the double sided as I think it gives the most professional look: One side with name, titel, phone, e-mail - then a little space - and four additional lines for address.
This composition is if all information should be in the same "column" - feel free to provide suggestions with the address places elsewhere on the one side.
On the other side, I'm only thinkin' something with the logo.
I'd be happy to see different ideas re. the use of the orange contrast, placement of logo, etc.
I do not plan on changing the design of businees cards ever - as I think it is more serious keeping a concept and avoid rebranding - and I'm sure that you can deliver an ever-lasting logo for my company! Thanks :).
Let's play the rest by ear in the correspondance.
Target Market(s)
Executive level: CEOs, HR directors, communication managers/directors, business owners.
Industry/Entity Type
Management Consulting

```html
<!DOCTYPE html>
<html lang="en">
<head>
<meta charset="utf-8">
<title>BrookLedger – Business Cards</title>
<link rel="stylesheet" href="https://fonts.googleapis.com/css2?family=Tinos&family=Arimo:wght@400&display=swap">
<style>
  :root {
    --backdrop: #e4e1dc;
    --card-black: #0b0b0b;
    --card-black-soft: #1c1c1c;
    --edge-grey: #3a3a3a;
    --orange: #f08a22;
    --orange-light: #f6982f;
    --white: #f4f4f4;
    --grey-name: #6f6f6f;
    --grey-title: #3b3b3b;
    --grey-tagline: #8a8a8a;
  }
  * { margin: 0; padding: 0; box-sizing: border-box; }
  html, body {
    width: 1200px;
    height: 1200px;
    overflow: hidden;
    background: var(--backdrop);
  }
  .sheet {
    position: relative;
    width: 1200px;
    height: 1200px;
  }
  .card {
    position: absolute;
    left: 150px;
    width: 900px;
    height: 514px;
    overflow: hidden;
    box-shadow: 0 10px 30px rgba(0, 0, 0, 0.25);
  }
  .card--front { top: 60px; }
  .card--back {
    top: 626px;
    background: radial-gradient(ellipse at 40% 30%, var(--card-black-soft), var(--card-black) 70%);
  }
  .card__shapes {
    position: absolute;
    inset: 0;
    width: 100%;
    height: 100%;
  }
  .logo {
    position: absolute;
    font-family: "Tinos", "Times New Roman", serif;
    color: var(--white);
    white-space: nowrap;
  }
  .logo__name {
    display: block;
    line-height: 1;
    letter-spacing: 0.5px;
  }
  .logo__tagline {
    display: block;
    color: var(--grey-tagline);
    text-align: right;
    text-transform: none;
  }
  .card--front .logo {
    left: 52px;
    top: 262px;
  }
  .card--front .logo__name { font-size: 58px; }
  .card--front .logo__tagline {
    font-size: 14px;
    letter-spacing: 4px;
    margin-top: 4px;
  }
  .card--back .logo {
    left: 50%;
    top: 50%;
    transform: translate(-50%, -55%);
  }
  .card--back .logo__name { font-size: 118px; }
  .card--back .logo__tagline {
    font-size: 22px;
    letter-spacing: 9px;
    margin-top: 6px;
  }
  .holder {
    position: absolute;
    right: 48px;
    top: 38px;
    text-align: right;
    font-family: "Arimo", Arial, sans-serif;
    line-height: 1.15;
  }
  .holder__name {
    font-size: 46px;
    color: var(--grey-name);
  }
  .holder__title {
    font-size: 34px;
    color: var(--grey-title);
  }
  .contact {
    position: absolute;
    left: 582px;
    top: 262px;
    list-style: none;
    font-family: "Arimo", Arial, sans-serif;
    font-size: 30px;
    color: var(--white);
  }
  .contact__item {
    display: flex;
    align-items: center;
    gap: 16px;
    height: 50px;
  }
  .contact__icon {
    width: 30px;
    height: 30px;
    flex: none;
    fill: var(--white);
  }
</style>
</head>
<body>
<main class="sheet">

  <section class="card card--front" aria-label="Business card front">
    <svg class="card__shapes" viewBox="0 0 900 514" preserveAspectRatio="none" aria-hidden="true">
      <defs>
        <linearGradient id="orange-panel" x1="0" y1="0" x2="1" y2="1">
          <stop offset="0" stop-color="var(--orange)"/>
          <stop offset="1" stop-color="var(--orange-light)"/>
        </linearGradient>
        <radialGradient id="black-panel" cx="0.3" cy="0.4" r="0.7">
          <stop offset="0" stop-color="#1a1a1a"/>
          <stop offset="1" stop-color="#070707"/>
        </radialGradient>
      </defs>
      <rect width="900" height="514" fill="url(#black-panel)"/>
      <path d="M 386 0 Q 470 240 494 514 L 900 514 L 900 0 Z" fill="var(--edge-grey)"/>
      <path d="M 400 0 Q 486 240 510 514 L 900 514 L 900 0 Z" fill="url(#orange-panel)"/>
    </svg>

    <div class="logo">
      <span class="logo__name">BrookLedger</span>
      <span class="logo__tagline">Guiding Dialogue</span>
    </div>

    <div class="holder">
      <p class="holder__name">Name</p>
      <p class="holder__title">Title</p>
    </div>

    <ul class="contact">
      <li class="contact__item">
        <svg class="contact__icon" viewBox="0 0 24 24" aria-hidden="true">
          <path d="M6.6 10.8a15.1 15.1 0 0 0 6.6 6.6l2.2-2.2a1 1 0 0 1 1-.25 11.4 11.4 0 0 0 3.6.57 1 1 0 0 1 1 1V20a1 1 0 0 1-1 1A17 17 0 0 1 3 4a1 1 0 0 1 1-1h3.5a1 1 0 0 1 1 1c0 1.25.2 2.45.57 3.57a1 1 0 0 1-.25 1z"/>
        </svg>
        <span>phone</span>
      </li>
      <li class="contact__item">
        <svg class="contact__icon" viewBox="0 0 24 24" aria-hidden="true">
          <path d="M2 5h20v2.2l-10 6.3L2 7.2z M2 9.6l10 6.3 10-6.3V19H2z"/>
        </svg>
        <span>e-mail</span>
      </li>
      <li class="contact__item">
        <svg class="contact__icon" viewBox="0 0 24 24" aria-hidden="true">
          <path d="M12 2a7 7 0 0 0-7 7c0 5.2 7 13 7 13s7-7.8 7-13a7 7 0 0 0-7-7zm0 9.5A2.5 2.5 0 1 1 12 6.5a2.5 2.5 0 0 1 0 5z"/>
        </svg>
        <span>address</span>
      </li>
    </ul>
  </section>

  <section class="card card--back" aria-label="Business card back">
    <div class="logo">
      <span class="logo__name">BrookLedger</span>
      <span class="logo__tagline">Guiding Dialogue</span>
    </div>
  </section>

</main>
</body>
</html>
```